Book cover design for the book titled "Quieter Under Lanterns."

create a book cover. The book title is, "Quieter Under Lanterns: A Ledger of Harbour Songs Across Mild Winters." The purpose of the book is to create awareness of how childhood trauma is impacting 7 out of 10 adults in the world today and that two-thirds of children will experience neglect and or abuse before their 18th birthday. One victim described that his mental and physical illness resulting from childhood trauma felt like he wa being pulled to the ground, that the force was "quieter under lanterns." The design should be clean and simple and communicate a crisis.

```html
<!DOCTYPE html>
<html lang="en">
<head>
<meta charset="UTF-8">
<title>Quieter Under Lanterns — Book Cover</title>
<link rel="stylesheet" href="https://fonts.googleapis.com/css2?family=Montserrat:wght@600;700;800&family=Noticia+Text:ital@1&display=swap">
<style>
  :root {
    --coral: #f96b5f;
    --ink: #000000;
    --paper: #ffffff;
  }
  * { margin: 0; padding: 0; box-sizing: border-box; }
  html, body {
    width: 1200px;
    height: 1200px;
    overflow: hidden;
    background: var(--paper);
  }
  .cover {
    position: absolute;
    left: 222px;
    top: 31px;
    width: 762px;
    height: 1143px;
    background: var(--coral);
    overflow: hidden;
  }
  .title {
    position: absolute;
    left: 0;
    top: 48px;
    width: 100%;
    text-align: center;
    font-family: "Montserrat", sans-serif;
    font-weight: 700;
    font-size: 116px;
    line-height: 120px;
    letter-spacing: -3px;
    text-transform: uppercase;
  }
  .title-line { display: block; }
  .title-line--light { color: var(--paper); }
  .title-line--dark { color: var(--ink); }
  .subtitle {
    position: absolute;
    left: 130px;
    top: 454px;
    width: 504px;
    height: 97px;
    border-top: 1px solid rgba(255,255,255,0.55);
    border-bottom: 1px solid rgba(255,255,255,0.55);
    display: flex;
    align-items: center;
    justify-content: center;
    text-align: center;
    font-family: "Noticia Text", serif;
    font-style: italic;
    font-size: 34px;
    line-height: 44px;
    color: var(--ink);
  }
  .hill-scene {
    position: absolute;
    left: 0;
    top: 0;
    width: 762px;
    height: 1143px;
  }
  .author {
    position: absolute;
    left: 0;
    bottom: 62px;
    width: 100%;
    padding-left: 14px;
    text-align: center;
    font-family: "Montserrat", sans-serif;
    font-weight: 600;
    font-size: 49px;
    letter-spacing: 2px;
    color: var(--paper);
  }
</style>
</head>
<body>
  <main class="cover">
    <svg class="hill-scene" viewBox="0 0 762 1143" role="img" aria-label="Illustration: a dark hillside slope with a large boulder rolling down toward a small fleeing figure">
      <polygon points="0,646 762,1027 762,1143 0,1143" fill="var(--ink)"/>
    </svg>

    <h1 class="title">
      <span class="title-line title-line--light">Quieter</span>
      <span class="title-line title-line--light">Under</span>
      <span class="title-line title-line--dark">Lanterns</span>
    </h1>

    <p class="subtitle">A Ledger of Harbour Songs<br>Across Mild Winters</p>

    <p class="author">AUTHOR NAME</p>
  </main>
</body>
</html>
```